Brava Set CEO and Partners Business Card

We need a fresh, fun, simple and clean business card design....we would like a template where we can add a name and title (as well as specific email addresses). We are open to different looks (full logo on one side and a small logo on the company info side, or our logo is in the background but faint on one side but full on the other, or something else cool :-) ). Our colors are in our logo: blue, black and white...however we are not opposed to the use of other colors if it works. We build sets, make props and a host of other things for the film and television industry...our card should reflect creativity, style and professionalism.

A white background would be preferred.

I would like to see an option with Facebook and Instagram icons.

Facebook- facebook.com/bravasetny
Instagram- brava_set

Our website is bravaset-example.com.

Brava Set, Inc.
418 Corvell Avenue, Unit 9
North Hollywood, California 91602
555.210.4873 | tel
555.210.6692 | fax
www.BravaSet-example.com

Sample Name and Title #1:

Peter Halvik
CEO / Co-Owner
555.210.4873 | tel
555.210.6692 | fax
peter@bravaset-example.com
www.BravaSet-example.com

Target Market(s)

Marketing Professionals, Production Designers, Interior Designers, Film Producers, Directors, Art Directors, Event Directors

Industry/Entity Type

Entertainment Industry

Contact Information for Business Card

Peter Halvik
CEO / Co-Owner
555.210.4873 | tel
555.210.6692 | fax
peter@bravaset-example.com
www.BravaSet-example.com

Font styles to use
Sans Serif

Colors
33a6d7
ffffff
1b1b1b

Requirements
Must have
• Logo, All Contact Info, White Background. Symmetry.
Nice to have
• Facebook and Instagram icons with addresses
• Facebook- facebook.com/bravasetny
• Instagram- brava_set

```html
<!DOCTYPE html>
<html lang="en">
<head>
<meta charset="utf-8">
<title>Brava Set – Business Card</title>
<link rel="stylesheet" href="https://fonts.googleapis.com/css2?family=Lato:wght@300;400;700;900&display=swap">
<style>
  :root {
    --brand-blue: #33a6d7;
    --brand-black: #1b1b1b;
    --card-white: #ffffff;
    --paper-grey: #f1f1f1;
    --stage: #d8d3cb;
    --ink-soft: #3a3a3a;
  }
  * { box-sizing: border-box; margin: 0; padding: 0; }
  html, body {
    width: 1200px;
    height: 780px;
    overflow: hidden;
  }
  body {
    background: var(--stage);
    font-family: "Lato", Arial, sans-serif;
    position: relative;
  }
  .card {
    position: absolute;
    top: 235px;
    width: 540px;
    height: 309px;
    border-radius: 16px;
    overflow: hidden;
    box-shadow: 0 10px 28px rgba(0,0,0,0.25);
  }
  .card--front {
    left: 40px;
    background: linear-gradient(160deg, var(--card-white) 0%, var(--paper-grey) 100%);
  }
  .card--back {
    left: 620px;
    background: var(--brand-black);
  }
  .wave {
    position: absolute;
    inset: 0;
    width: 100%;
    height: 100%;
  }
  .wordmark {
    font-weight: 900;
    letter-spacing: 1px;
    line-height: 1;
    white-space: nowrap;
  }
  .wordmark--front {
    position: absolute;
    right: 40px;
    top: 38px;
    font-size: 52px;
    color: var(--brand-black);
  }
  .wordmark--back {
    position: absolute;
    left: 0;
    right: 0;
    top: 50%;
    transform: translateY(-50%);
    text-align: center;
    font-size: 76px;
    color: var(--card-white);
  }
  .address {
    position: absolute;
    right: 40px;
    top: 112px;
    text-align: right;
    font-size: 13px;
    line-height: 1.45;
    color: var(--ink-soft);
  }
  .website {
    position: absolute;
    right: 34px;
    bottom: 24px;
    font-size: 12px;
    letter-spacing: 0.3px;
    color: var(--card-white);
  }
  .website .accent { color: var(--brand-blue); }
  .identity {
    position: absolute;
    left: 36px;
    top: 64px;
  }
  .identity__name {
    font-size: 19px;
    font-weight: 700;
    letter-spacing: 0.5px;
    text-transform: uppercase;
    color: var(--brand-black);
  }
  .identity__title {
    font-size: 15px;
    font-weight: 400;
    color: var(--brand-blue);
    margin-top: 2px;
  }
  .social {
    position: absolute;
    left: 36px;
    top: 128px;
    display: flex;
    gap: 8px;
  }
  .social__tile {
    width: 17px;
    height: 17px;
    border-radius: 3px;
    background: var(--brand-blue);
  }
  .contacts {
    position: absolute;
    left: 104px;
    top: 160px;
    list-style: none;
  }
  .contacts__item {
    display: flex;
    align-items: center;
    gap: 9px;
    font-size: 14px;
    line-height: 1;
    color: var(--ink-soft);
    margin-bottom: 6px;
  }
  .contacts__icon {
    width: 16px;
    height: 16px;
    flex: none;
  }
</style>
</head>
<body>

  <section class="card card--front" aria-label="Business card, front">
    <svg class="wave" viewBox="0 0 540 309" preserveAspectRatio="none" aria-hidden="true">
      <path d="M540,178 C470,180 430,200 382,240 C320,292 200,300 0,302 L0,309 L540,309 Z" fill="#1b1b1b"/>
      <path d="M30,301 C190,296 310,276 372,228 C396,208 408,196 420,190 C398,214 380,232 356,250 C290,292 180,302 30,301 Z" fill="#33a6d7"/>
    </svg>

    <div class="wordmark wordmark--front">Brava Set</div>

    <address class="address">
      418 Corvell Avenue, Unit 9<br>
      North Hollywood, California 91602
    </address>

    <div class="website">www.<span class="accent">BravaSet-example</span>.com</div>

    <div class="identity">
      <div class="identity__name">Peter Halvik</div>
      <div class="identity__title">CEO / Co-Owner</div>
    </div>

    <div class="social" aria-label="Social links">
      <span class="social__tile"></span>
      <span class="social__tile"></span>
    </div>

    <ul class="contacts">
      <li class="contacts__item">
        <svg class="contacts__icon" viewBox="0 0 16 16" aria-hidden="true">
          <rect width="16" height="16" rx="3" fill="#33a6d7"/>
          <path d="M5 3.5 L6.8 3.5 L7.4 6 L6.3 6.9 C6.9 8.3 7.8 9.2 9.1 9.8 L10 8.7 L12.5 9.3 L12.5 11 C12.5 11.8 11.8 12.5 11 12.5 C7.4 12.2 3.8 8.6 3.5 5 C3.5 4.2 4.2 3.5 5 3.5 Z" fill="#ffffff"/>
        </svg>
        555.210.4873
      </li>
      <li class="contacts__item">
        <svg class="contacts__icon" viewBox="0 0 16 16" aria-hidden="true">
          <rect width="16" height="16" rx="3" fill="#33a6d7"/>
          <rect x="5" y="3" width="6" height="3.5" fill="#ffffff"/>
          <rect x="3" y="6.5" width="10" height="4.5" rx="1" fill="#ffffff"/>
          <rect x="5" y="10" width="6" height="3" fill="#ffffff" stroke="#33a6d7" stroke-width="0.8"/>
        </svg>
        555.210.6692
      </li>
      <li class="contacts__item">
        <svg class="contacts__icon" viewBox="0 0 16 16" aria-hidden="true">
          <rect width="16" height="16" rx="3" fill="#33a6d7"/>
          <rect x="3" y="4.5" width="10" height="7" fill="#ffffff"/>
          <path d="M3 4.5 L8 8.5 L13 4.5" fill="none" stroke="#33a6d7" stroke-width="1"/>
        </svg>
        peter@bravaset-example.com
      </li>
    </ul>
  </section>

  <section class="card card--back" aria-label="Business card, back">
    <div class="wordmark wordmark--back">Brava Set</div>
  </section>

</body>
</html>
```